Business Card Design Project - KLB

I am looking for a more sophisticated card design for my company,
"The Kestrel Bureau"

We are a consultancy focused on strategy and change in Associations and professional organisations.

I am a lawyer and psychologist with a PhD and so am looking for something that communicates seriousness and credibility but also quirky creative solutions for strategic problems, which is my field of speciality.

I am looking for something that is quietly spoken, rather than loud colours ('credible' and 'creative' are the two adjectives that I think of as competing here).

I particularly like an embossed card style - heavy white card with plain white or white and black or white and grey text.

The key logo image for the company is a question mark and I am open to suggestions and ideas on design.

I have attached a file that includes a couple of styles that have caught my eye and my thoughts on them. Hopefully they communicate what I'm looking for.
Updates

Thank you for all the great suggestions and designs.

I really appreciated the effort and creative energy you put into your designs. I have now closed the project after selecting a design and advising the successful designer of the card that I am happy with.

Regards

Target Market(s)

Organisations (CEO's and Boards), Governments, Legal professionals, Membership Associations and aspiring professionals.

Industry/Entity Type

Lawyer

Requirements
Must have
• The key logo element is a question mark (?) and this needs to be incorporated.

Embossed style - cut outs or other design ideas interest me too.

The attached file has a number of sample ideas and comments on each one that I like.
Should not have
• I like crisp, modern fonts (Myriads etc...) and do not like embellished fonts or Times etc...

```html
<!DOCTYPE html>
<html lang="en">
<head>
<meta charset="utf-8">
<title>The Kestrel Bureau — Business Card</title>
<link rel="stylesheet" href="https://fonts.googleapis.com/css2?family=Arimo:wght@700&family=Jost:wght@300&family=Lato:wght@400&display=swap">
<style>
  :root {
    --paper: #ffffff;
    --card-white: #ffffff;
    --card-grey: #d1d3d4;
    --edge: #231f20;
    --ink: #231f20;
    --ink-soft: #58595b;
    --wordmark: #939598;
    --accent: #d7df3f;
  }
  html, body {
    margin: 0;
    padding: 0;
    width: 1200px;
    height: 1200px;
    overflow: hidden;
    background: var(--paper);
  }
  .sheet {
    position: relative;
    width: 1200px;
    height: 1200px;
  }
  .card {
    position: absolute;
    width: 598px;
    height: 341px;
    display: block;
  }
  .card--front { left: 315px; top: 203px; }
  .card--back  { left: 324px; top: 623px; }
  .card__face  { fill: var(--card-white); }
  .card__sweep { fill: var(--card-grey); }
  .card__edge  { fill: none; stroke: var(--edge); stroke-width: 2.5; }
  .wordmark {
    font-family: "Arimo", Arial, sans-serif;
    font-weight: 700;
    fill: var(--wordmark);
  }
  .wordmark__dot { fill: var(--accent); }
  .holder__name {
    font-family: "Jost", "Helvetica Neue", sans-serif;
    font-weight: 300;
    font-size: 22px;
    fill: var(--ink-soft);
    letter-spacing: -0.3px;
  }
  .holder__role {
    font-family: "Jost", "Helvetica Neue", sans-serif;
    font-weight: 300;
    font-size: 19px;
    fill: var(--ink-soft);
  }
  .contact {
    font-family: "Lato", "Gill Sans", sans-serif;
    font-weight: 400;
    font-size: 14.5px;
    fill: var(--ink);
  }
</style>
</head>
<body>
<main class="sheet">

  <svg class="card card--front" viewBox="0 0 598 341" aria-label="Business card, front">
    <rect class="card__face" x="0" y="0" width="598" height="341"/>
    <path class="card__sweep" d="M243,0 C317,60 360,146 345,206 C336,257 313,300 282,341 L598,341 L598,0 Z"/>
    <circle class="wordmark__dot" cx="152" cy="184" r="11"/>
    <text class="wordmark" x="174" y="198" font-size="40">The Kestrel Bureau</text>
    <rect class="card__edge" x="1.25" y="1.25" width="595.5" height="338.5"/>
  </svg>

  <svg class="card card--back" viewBox="0 0 598 341" aria-label="Business card, back">
    <rect class="card__face" x="0" y="0" width="598" height="341"/>
    <path class="card__sweep" d="M242,0 C318,60 362,140 347,190 C338,248 317,296 286,341 L598,341 L598,0 Z"/>
    <circle class="wordmark__dot" cx="63" cy="185" r="8"/>
    <text class="wordmark" x="77" y="195" font-size="27">The Kestrel Bureau</text>

    <text class="holder__name" x="583" y="57" text-anchor="end">Dr. Mara Holloway</text>
    <text class="holder__role" x="583" y="83" text-anchor="end">Director</text>

    <g class="contact" text-anchor="middle">
      <text x="469" y="147">Mobile:+ 61400 372 915</text>
      <text x="469" y="167">Phone:+ 612 9034 6217</text>
      <text x="469" y="187">E-mail: mara@kestrelbureau.com.au</text>
      <text x="469" y="219">P.O Box 4180, Elmwood Park,</text>
      <text x="469" y="240">Sydney, Australia</text>
    </g>
    <rect class="card__edge" x="1.25" y="1.25" width="595.5" height="338.5"/>
  </svg>

</main>
</body>
</html>
```